Verpackungen für ein CBD Öl
Zielgruppe
Wir bringen ein neues CBD Öl auf den Markt. Unsere Zielgruppe sind Männer und Frauen ab 18 Jahren die natürliche Produkte den 'Chemischen' bevorzugen.
Aufgabenstellung
Es soll bitte eine Faltschachteln für ein CBD Öl designt werden. Die Stanzvorlage habe ich hochgeladen. Als Name des CBD Öls bitte erstmal 'XX' nehmen. Wir werden den Namen zu einem späteren Zeitpunkt nennen. Wichtig ist, dass das Design modern und eher 'edel' aussieht.
Die Pflichttexte, Namen, Barcode etc. können zu einem späteren Zeitpunkt hinzugefügt werden.
Es geht erstmal nur um ein schönes Design :-)

```html
<!DOCTYPE html>
<html lang="de">
<head>
<meta charset="utf-8">
<title>CBD Öl Mild – Faltschachtel</title>
<link href="https://fonts.googleapis.com/css2?family=Mulish:wght@400;500;700&display=swap" rel="stylesheet">
<style>
  :root {
    --backdrop: #d9d9d9;
    --box-green: #4d5d48;
    --box-green-dark: #3b4637;
    --band-dark: #323c30;
    --leaf-light: #6a7f60;
    --leaf-mid: #566a4f;
    --seal-fill: #3d4a39;
    --gold: #d9b453;
    --ink-light: #f2f2ee;
  }
  * { margin: 0; padding: 0; box-sizing: border-box; }
  html, body { width: 1200px; height: 983px; overflow: hidden; }
  body {
    background: var(--backdrop);
    font-family: "Mulish", sans-serif;
    position: relative;
  }
  .carton-front {
    position: absolute;
    left: 445px; top: 32px;
    width: 310px; height: 920px;
    background: linear-gradient(180deg, var(--box-green) 0%, #475643 60%, var(--box-green-dark) 100%);
    overflow: hidden;
    color: var(--ink-light);
  }
  .leaf-backdrop {
    position: absolute;
    left: 0; top: 394px; width: 310px; height: 310px;
    background:
      radial-gradient(ellipse 60% 35% at 30% 30%, rgba(106,127,96,0.85) 0%, rgba(106,127,96,0) 100%),
      radial-gradient(ellipse 70% 40% at 65% 70%, rgba(106,127,96,0.8) 0%, rgba(106,127,96,0) 100%),
      linear-gradient(180deg, rgba(86,106,79,0) 0%, var(--leaf-mid) 35%, var(--leaf-mid) 85%, rgba(86,106,79,0.6) 100%);
  }
  .dark-band {
    position: absolute;
    left: 0; top: 706px; width: 310px; height: 64px;
    background: var(--band-dark);
  }
  .brand-line {
    position: absolute; top: 44px; width: 100%;
    text-align: center; font-size: 34px; font-weight: 500; letter-spacing: 1px;
  }
  .seal {
    position: absolute; left: 25px; top: 164px; width: 260px; height: 260px;
    border-radius: 50%;
    background: var(--seal-fill);
    display: flex; align-items: center; justify-content: center;
  }
  .seal-name {
    font-size: 46px; font-weight: 400; letter-spacing: 2px;
    color: var(--gold);
  }
  .product-name {
    position: absolute; top: 482px; width: 100%;
    text-align: center; font-size: 39px; font-weight: 400;
  }
  .rule {
    position: absolute; left: 18px; width: 270px; height: 2px;
    background: var(--gold);
  }
  .rule-top { top: 539px; }
  .rule-bottom { top: 580px; }
  .strength {
    position: absolute; top: 545px; width: 100%;
    text-align: center; font-size: 24px; font-weight: 700; letter-spacing: 7px;
    padding-left: 7px;
    color: var(--gold);
  }
  .dose {
    position: absolute; left: 26px; top: 876px; font-size: 16px;
  }
  .maker {
    position: absolute; left: 213px; width: 80px; top: 846px; text-align: center;
    font-size: 16px; font-weight: 700;
  }
  .volume {
    position: absolute; left: 213px; width: 80px; top: 876px; text-align: center; font-size: 16px;
  }
</style>
</head>
<body>
  <main class="carton-front">
    <div class="leaf-backdrop" role="img" aria-label="Faint hemp leaf illustration in muted green"></div>
    <div class="dark-band"></div>

    <div class="brand-line">XXX</div>

    <div class="seal"><span class="seal-name">XXXX</span></div>

    <div class="product-name">CBD ÖL</div>
    <div class="rule rule-top"></div>
    <div class="strength">MILD</div>
    <div class="rule rule-bottom"></div>

    <div class="dose">2000mg CBD</div>
    <div class="maker">Elmwald</div>
    <div class="volume">10 ml</div>
  </main>
</body>
</html>
```